Business card design for Automotive workshop

We need a business card for a new automotive repair and tyre shop called Ridgeback Prime Automotive located in New Zealand. We are a clean, modern and fresh workshop and company.

Front needs to feature logo,
my name:
Lachie Westergaard (director)

Address:
48 Marlow Lane
Kowhai Bay 3592

Phone: 07 842 1937
Mobile: 027 519 2764
Email: office@ridgebackmotors.co.nz
Website: ridgebackmotors.co.nz

Back needs to feature an area to write down appointment details, date and time.

Also feature a list of jobs and work we do such as,
Vehicle Servicing
All Mechanical Repairs
Warrant of Fitness
Tyres & Wheel Alignments
Automotive Diagnostics
Automotive Parts & Supplies

```html
<!DOCTYPE html>
<html lang="en">
<head>
<meta charset="utf-8">
<title>Ridgeback Prime Automotive – Business Card</title>
<link rel="stylesheet" href="https://fonts.googleapis.com/css2?family=Lato:wght@400;700;900&display=swap">
<style>
  :root {
    --bg: #2b2b2b;
    --card-white: #ffffff;
    --card-dark: #3a3a3c;
    --brand-red: #e0212e;
    --ink: #4a4a4a;
    --ink-soft: #7a7a7a;
    --on-dark: #d8d8d8;
  }
  * { box-sizing: border-box; margin: 0; padding: 0; }
  html, body {
    width: 1200px; height: 900px; overflow: hidden;
    background: var(--bg);
    font-family: "Lato", Arial, sans-serif;
  }
  .canvas {
    width: 1200px; height: 900px;
    display: flex; flex-direction: column; align-items: center; justify-content: center;
    gap: 34px;
  }
  .card {
    width: 700px; height: 400px; position: relative; overflow: hidden;
    background: var(--card-white);
    box-shadow: 0 10px 30px rgba(0,0,0,.45);
  }
  .wordmark {
    font-weight: 900; text-transform: uppercase; color: var(--brand-red);
    letter-spacing: 1px; line-height: 1.1;
  }

  /* Front */
  .front .wordmark {
    position: absolute; right: 46px; top: 118px;
    font-size: 26px; text-align: right; white-space: nowrap;
  }
  .holder { position: absolute; left: 46px; top: 120px; }
  .holder-name { font-size: 32px; font-weight: 700; color: var(--brand-red); white-space: nowrap; }
  .holder-role { font-size: 16px; color: var(--ink-soft); margin-top: 2px; }
  .front .rule {
    position: absolute; left: 46px; right: 46px; top: 228px;
    height: 1.5px; background: var(--brand-red);
  }
  .contacts {
    position: absolute; left: 46px; right: 46px; top: 252px;
    display: flex; justify-content: space-between;
    font-size: 16px; color: var(--ink);
  }
  .contact-col { display: flex; flex-direction: column; gap: 8px; }
  .contact-item { display: flex; align-items: center; gap: 8px; white-space: nowrap; }
  .contact-item svg { width: 13px; height: 13px; fill: var(--brand-red); flex: none; }
  .address { font-size: 20px; line-height: 1.3; }
  .address svg { width: 14px; height: 16px; align-self: flex-start; margin-top: 4px; }

  /* Back */
  .back .top {
    position: absolute; left: 0; right: 0; top: 0; height: 196px;
    background: var(--card-dark);
    border-bottom: 4px solid var(--brand-red);
    display: flex; flex-direction: column; align-items: flex-end;
    padding: 34px 46px 0;
  }
  .back .wordmark { font-size: 30px; white-space: nowrap; }
  .services {
    margin-top: 14px; text-align: right;
    font-size: 15px; color: var(--on-dark); line-height: 1.5;
  }
  .services .sep { color: var(--brand-red); padding: 0 4px; }
  .appointment {
    position: absolute; left: 46px; right: 46px; top: 240px;
  }
  .appointment-title {
    text-align: center; color: var(--brand-red); font-size: 17px; margin-bottom: 40px;
  }
  .fields { display: flex; gap: 40px; }
  .field {
    flex: 1; display: flex; align-items: flex-end; gap: 8px;
    font-size: 15px; color: var(--ink-soft);
  }
  .field .blank { flex: 1; border-bottom: 1px dashed var(--ink-soft); height: 16px; }
</style>
</head>
<body>
<main class="canvas">

  <section class="card front" aria-label="Card front">
    <div class="holder">
      <p class="holder-name">Lachie Westergaard</p>
      <p class="holder-role">Director</p>
    </div>

    <div class="wordmark">Ridgeback Prime<br>Automotive</div>

    <div class="rule"></div>

    <div class="contacts">
      <div class="contact-col">
        <div class="contact-item">
          <svg viewBox="0 0 24 24" aria-hidden="true"><path d="M6.6 10.8a15.1 15.1 0 0 0 6.6 6.6l2.2-2.2a1 1 0 0 1 1-.25 11.4 11.4 0 0 0 3.6.57 1 1 0 0 1 1 1V20a1 1 0 0 1-1 1A17 17 0 0 1 3 4a1 1 0 0 1 1-1h3.5a1 1 0 0 1 1 1c0 1.25.2 2.45.57 3.57a1 1 0 0 1-.25 1z"/></svg>
          <span>07 842 1937</span>
        </div>
        <div class="contact-item">
          <svg viewBox="0 0 24 24" aria-hidden="true"><path d="M7 1h10a2 2 0 0 1 2 2v18a2 2 0 0 1-2 2H7a2 2 0 0 1-2-2V3a2 2 0 0 1 2-2zm0 3v14h10V4z"/></svg>
          <span>027 519 2764</span>
        </div>
      </div>
      <div class="contact-col">
        <div class="contact-item">
          <svg viewBox="0 0 24 24" aria-hidden="true"><path d="M2 5h20v14H2zm2 2v.5l8 5 8-5V7z"/></svg>
          <span>office@ridgebackmotors.co.nz</span>
        </div>
        <div class="contact-item">
          <svg viewBox="0 0 24 24" aria-hidden="true"><circle cx="12" cy="12" r="10"/></svg>
          <span>www.ridgebackmotors.co.nz</span>
        </div>
      </div>
      <div class="contact-col">
        <div class="contact-item address">
          <svg viewBox="0 0 24 28" aria-hidden="true"><path d="M12 0a9 9 0 0 1 9 9c0 7-9 19-9 19S3 16 3 9a9 9 0 0 1 9-9zm0 5a4 4 0 1 0 0 8 4 4 0 0 0 0-8z"/></svg>
          <span>48 Marlow Lane<br>Kowhai Bay 3592</span>
        </div>
      </div>
    </div>
  </section>

  <section class="card back" aria-label="Card back">
    <div class="top">
      <div class="wordmark">Ridgeback Prime Automotive</div>
      <div class="services">
        <p>Vehicle Servicing<span class="sep">/</span>All Mechanical Repairs</p>
        <p>Warrant of Fitness<span class="sep">/</span>Tyres &amp; Wheel Alignments</p>
        <p>Automotive Diagnostics<span class="sep">/</span>Automotive Parts &amp; Supplies</p>
      </div>
    </div>

    <div class="appointment">
      <p class="appointment-title">Appointment</p>
      <div class="fields">
        <div class="field"><span>Date</span><span class="blank"></span></div>
        <div class="field"><span>Time</span><span class="blank"></span></div>
      </div>
    </div>
  </section>

</main>
</body>
</html>
```